Powerpoint Slide Deck

I had my logo designed using drafthollow and would like to have a professional looking powerpoint deck created with my logo etc. my website is vantreo.info

```html
<!DOCTYPE html>
<html lang="en">
<head>
<meta charset="utf-8">
<title>Vantreo – Slide Deck</title>
<link href="https://fonts.googleapis.com/css2?family=Exo+2:wght@500;600;700&family=Lora:wght@400&display=swap" rel="stylesheet">
<style>
:root{
  --canvas:#3a3b3d;
  --paper:#f4f5f8;
  --ink:#141414;
  --muted:#555a60;
  --green:#7fbd3a;
  --green-soft:#b9dd95;
  --green-pale:#d6ecc0;
  --navy:#0d1547;
  --violet:#3b2bc4;
  --teal:#0f2a33;
  --white:#ffffff;
  --grey-disc:#e9eaec;
}
*{box-sizing:border-box;margin:0;padding:0}
html,body{width:1200px;height:4082px;overflow:hidden;background:var(--canvas)}
body{position:relative;font-family:"Lora",serif;color:var(--ink)}
.slide{position:absolute;left:74px;width:1052px;height:591px;overflow:hidden;background:var(--paper)}
.s1{top:74px}.s2{top:740px}.s3{top:1409px}.s4{top:2077px}.s5{top:2747px}.s6{top:3416px}
.abs{position:absolute}
.head{font-family:"Exo 2",sans-serif;font-weight:700;color:var(--ink);letter-spacing:.5px}
.brand{position:absolute;right:35px;top:34px;display:flex;flex-direction:column;align-items:center;font-family:"Exo 2",sans-serif;font-weight:500;font-size:24px;color:var(--ink)}
.brand .dot{width:18px;height:18px;border-radius:50%;background:var(--green);margin-bottom:4px}
.brand.light{color:var(--white)}
/* slide 1 */
.hero-photo{position:absolute;inset:0;background:radial-gradient(circle at 50% 45%,#5a2be0 0,#3a1fb0 22%,#151a66 45%,#080b2c 80%)}
.hero-title{position:absolute;left:0;right:0;text-align:center;color:var(--white);font-family:"Exo 2",sans-serif;font-weight:700}
/* slide 2 */
.welcome-title{left:552px;top:230px;font-size:36px}
.body-copy{font-size:12px;line-height:22px;color:var(--muted)}
/* slide 3 */
.sol-title{left:72px;top:102px;font-size:32px}
.sol-item{position:absolute;left:72px;display:flex;gap:14px;align-items:flex-start}
.sol-thumb{width:70px;height:70px;border-radius:50%;background:linear-gradient(135deg,#1f3b78,#6a86b8);flex:none}
.sol-item h3{font-family:"Exo 2",sans-serif;font-weight:600;font-size:20px;margin:6px 0 4px}
.sol-item p{font-size:12px;line-height:19px;color:#333;width:270px}
/* slide 4 */
.partner-band{position:absolute;left:0;top:0;width:100%;height:349px;background:linear-gradient(180deg,#0b2430,#12323c 50%,#0a1c24)}
.partner-row{position:absolute;top:440px;left:0;width:100%}
.partner{position:absolute;transform:translateX(-50%);display:flex;align-items:center;gap:8px;font-family:"Exo 2",sans-serif;font-weight:600;font-size:20px;color:#333}
.partner i{display:block;width:18px;height:18px;background:#9aa0a8}
/* slide 5 */
.testi{position:absolute;top:172px;width:280px;height:280px;border-radius:50%;background:var(--grey-disc);text-align:center;padding:70px 26px 0}
.testi.featured{background:var(--green);color:var(--white)}
.testi p{font-size:9.5px;line-height:16px;color:#444}
.testi.featured p{color:var(--white)}
.testi h4{font-family:"Exo 2",sans-serif;font-weight:600;font-size:16px;margin-top:8px}
.testi span{font-size:9px;display:block;margin-top:4px}
.avatar{position:absolute;top:434px;width:58px;height:58px;border-radius:50%;border:3px solid var(--white);background:linear-gradient(135deg,#b98d74,#6b5446)}
/* slide 6 */
.contact{position:absolute;top:220px;display:flex;align-items:center;gap:14px;font-family:"Exo 2",sans-serif}
.contact .ic{width:48px;height:48px;border-radius:50%;background:var(--green);display:flex;align-items:center;justify-content:center}
.contact b{display:block;font-weight:600;font-size:15px}
.contact span{font-size:15px}
.end-brand{position:absolute;left:0;right:0;top:380px;display:flex;flex-direction:column;align-items:center;font-family:"Exo 2",sans-serif;font-weight:500;font-size:62px;color:var(--ink)}
.end-brand .dot{width:56px;height:56px;border-radius:50%;background:var(--green);margin-bottom:8px}
</style>
</head>
<body>

<section class="slide s1">
  <div class="hero-photo" role="img" aria-label="Data center server racks lit in blue and violet behind a glowing circle"></div>
  <div class="brand light"><span class="dot"></span>Vantreo</div>
  <h1 class="hero-title" style="top:186px;font-size:62px;letter-spacing:1px">VANTREO</h1>
  <p class="hero-title" style="top:270px;font-size:34px;line-height:48px">A CLEAR PATH TO IT<br>OPTIMIZATION</p>
</section>

<section class="slide s2">
  <svg class="abs" style="left:0;top:0" width="500" height="591" viewBox="0 0 500 591" role="img" aria-label="Two colleagues smiling while working at a computer">
    <defs><linearGradient id="g2" x1="0" y1="0" x2="1" y2="1"><stop offset="0" stop-color="#d9d4cc"/><stop offset=".6" stop-color="#8b6a4e"/><stop offset="1" stop-color="#3c3a38"/></linearGradient></defs>
    <path d="M0 0H496V260A240 240 0 0 1 256 500H0Z" fill="url(#g2)"/>
  </svg>
  <div class="brand"><span class="dot"></span>Vantreo</div>
  <h2 class="head abs welcome-title">WELCOME TO VANTREO</h2>
  <p class="body-copy abs" style="left:552px;top:288px;width:465px">In a complex world of IT Vantreo will assist you in optimizing IT spend. Our 20 plus years in the IT industry brings best of breed personnel from Data center, Managed Services, and Disaster Recovery, to help you get the best solutions for the best price.</p>
  <p class="body-copy abs" style="left:552px;top:376px">In a complex world of IT, let us help simplify.</p>
</section>

<section class="slide s3">
  <h2 class="head abs sol-title">OUR SOLUTIONS</h2>
  <div class="sol-item" style="top:178px"><div class="sol-thumb" role="img" aria-label="Cloud technology image"></div><div><h3>CLOUD</h3><p>In todays quickly changing IT environment companies have a lot of choices.</p></div></div>
  <div class="sol-item" style="top:275px"><div class="sol-thumb" role="img" aria-label="Team meeting image"></div><div><h3>MANAGED SERVICES</h3><p>Should you manage internally or should you hire an expert to manage?</p></div></div>
  <div class="sol-item" style="top:372px"><div class="sol-thumb" role="img" aria-label="Data center corridor image"></div><div><h3>DATA CENTER</h3><p>Should you be in the Data Center business?</p></div></div>
  <div class="abs" style="left:576px;top:0;width:440px;height:535px;background:var(--green-pale);border-bottom-left-radius:100px"></div>
  <div class="abs" style="left:596px;top:0;width:456px;height:515px;background:var(--green-soft);border-bottom-left-radius:90px"></div>
  <div class="abs" style="left:618px;top:0;width:434px;height:491px;background:linear-gradient(135deg,#1b1f26,#3a4250 55%,#c9ccd2);border-bottom-left-radius:80px" role="img" aria-label="Technician with a tablet checking cables in a server rack"></div>
  <div class="brand light"><span class="dot"></span>Vantreo</div>
</section>

<section class="slide s4">
  <div class="partner-band" role="img" aria-label="Dark server room with cable racks"></div>
  <div class="brand light"><span class="dot"></span>Vantreo</div>
  <h2 class="head abs" style="left:0;right:0;top:112px;text-align:center;color:var(--white);font-size:36px">OUR PARTNERS</h2>
  <p class="abs" style="left:240px;width:572px;top:168px;text-align:center;color:#dfe4e6;font-size:12px;line-height:21px">Lorem ipsum dolor sit amet, consectetur adipiscing elit, sed do eiusmod tempor incididunt ut labore et dolore magna aliqua. Quis ipsum suspendisse ultrices gravida. Risus commodo viverra maecenas accumsan lacus vel facilisis.</p>
  <div class="partner-row">
    <div class="partner" style="left:208px"><i></i>Northwire</div>
    <div class="partner" style="left:372px"><i></i>Skyvault</div>
    <div class="partner" style="left:523px"><i></i>Linkmesh</div>
    <div class="partner" style="left:672px"><i></i>Cloudharbor</div>
    <div class="partner" style="left:837px"><i></i>Gridsoft</div>
  </div>
</section>

<section class="slide s5">
  <div class="brand"><span class="dot"></span>Vantreo</div>
  <h2 class="head abs" style="left:0;right:0;top:46px;text-align:center;font-size:38px">CLIENT TESTIMONIAL</h2>
  <p class="abs" style="left:0;right:0;top:104px;text-align:center;font-family:'Exo 2',sans-serif;font-weight:700;font-size:13px">UNDER CONSTRUCTION!</p>
  <div class="testi" style="left:74px"><p>Lorem ipsum dolor sit amet, consectetur adipiscing elit, sed do eiusmod tempor incididunt ut labore et dolore magna aliqua. Quis ipsum suspendisse ultrices gravida. Risus commodo viverra maecenas accumsan lacus vel facilisis.</p><h4>Marla Quenby</h4><span>Lorem Ipsum</span></div>
  <div class="testi featured" style="left:385px"><p>Lorem ipsum dolor sit amet, consectetur adipiscing elit, sed do eiusmod tempor incididunt ut labore et dolore magna aliqua. Quis ipsum suspendisse ultrices gravida. Risus commodo viverra maecenas accumsan lacus vel facilisis.</p><h4>Sonia Pereth</h4><span>Lorem Ipsum</span></div>
  <div class="testi" style="left:696px"><p>Lorem ipsum dolor sit amet, consectetur adipiscing elit, sed do eiusmod tempor incididunt ut labore et dolore magna aliqua. Quis ipsum suspendisse ultrices gravida. Risus commodo viverra maecenas accumsan lacus vel facilisis.</p><h4>Tomas Ravik</h4><span>Design Lead</span></div>
  <div class="avatar" style="left:185px" role="img" aria-label="Client portrait"></div>
  <div class="avatar" style="left:496px" role="img" aria-label="Client portrait"></div>
  <div class="avatar" style="left:807px" role="img" aria-label="Client portrait"></div>
</section>

<section class="slide s6">
  <h2 class="head abs" style="left:0;right:0;top:126px;text-align:center;font-size:40px">THANK YOU</h2>
  <div class="contact" style="left:164px"><div class="ic"><svg width="20" height="24" viewBox="0 0 20 24"><path d="M10 0a9 9 0 0 0-9 9c0 7 9 15 9 15s9-8 9-15a9 9 0 0 0-9-9z" fill="#fff"/><circle cx="10" cy="9" r="3.5" fill="#7fbd3a"/></svg></div><div><b>Loaction</b><b>Vantreo United States</b></div></div>
  <div class="contact" style="left:453px"><div class="ic"><svg width="22" height="22" viewBox="0 0 24 24"><path d="M6.6 10.8a15 15 0 0 0 6.6 6.6l2.2-2.2a1 1 0 0 1 1-.25 11.4 11.4 0 0 0 3.6.57 1 1 0 0 1 1 1V20a1 1 0 0 1-1 1A17 17 0 0 1 3 4a1 1 0 0 1 1-1h3.5a1 1 0 0 1 1 1c0 1.25.2 2.45.57 3.57a1 1 0 0 1-.25 1z" fill="#fff"/></svg></div><div><b>Phone</b><span>+1 555 010 2040</span></div></div>
  <div class="contact" style="left:702px"><div class="ic"><svg width="22" height="18" viewBox="0 0 22 18"><rect x="1" y="2" width="20" height="14" rx="2" fill="#fff"/><path d="M2 3l9 7 9-7" fill="none" stroke="#7fbd3a" stroke-width="2"/></svg></div><div><b>Email</b><span>info@vantreo.info</span></div></div>
  <div class="end-brand"><span class="dot"></span>Vantreo</div>
</section>

</body>
</html>
```